Digital Agency Needs a Relaunch

We are looking for a modern, top-notch design to elevate our brand to win new clients. It has to build on the clarity of message in the current wireframes and must fit together well on Wordpress.

The winning designer will need to complete the other pages, but please focus on the homepage as the base of your proposed designs for us.

Use the existing logo as a point, and the colour scheme should be around that, we currently use these colours, but you can suggest new mixes:
Purple: #5c306b
Orange: #e27927
Grey: #5f4f61
Light grey: #cacaca
Off white: #ececec
Blue: #674ea7
Updates

Target Market(s)

Decent Sized SME Businesses (20+ Staff, Over £1m turnover)

Industry/Entity Type

Digital Marketing

Number of Pages Required

5+ page

Font styles to use
Sans Serif

Colors

Designer to choose colors to be used in the design.

Requirements
Must have
• A real attention on the design piece. Ignore the current website and really focus on the messaging and the brief.
Nice to have
• Read the messages and think about the impact. Use the purple in the logo more than the orange, but try to keep it smart rather than cool
Should not have
• Inconsistent design, serif fonts, stock images and not meeting the wireframes.

```html
<!DOCTYPE html>
<html lang="en">
<head>
<meta charset="utf-8">
<title>Vanta Digital – Growth Works</title>
<link href="https://fonts.googleapis.com/css2?family=Fira+Sans:ital,wght@0,300;0,400;0,500;0,600;1,300&display=swap" rel="stylesheet">
<style>
:root{
  --purple:#5c306b;
  --purple-deep:#3f1f7a;
  --violet:#4a2482;
  --orange:#e27927;
  --grey:#5f4f61;
  --light-grey:#cacaca;
  --off-white:#ececec;
  --blue:#674ea7;
  --ink:#1c1c1c;
  --white:#fff;
}
*{box-sizing:border-box;margin:0;padding:0}
html,body{width:1200px;height:4843px;overflow:hidden}
body{font-family:"Fira Sans",sans-serif;color:var(--ink);background:var(--white);position:relative}
a{color:inherit;text-decoration:none}
.abs{position:absolute}

/* header */
.site-header{position:absolute;top:0;left:0;width:1200px;height:88px;background:var(--white)}
.brand{position:absolute;left:88px;top:18px;display:flex;align-items:center;gap:10px;color:var(--purple);font-weight:500;font-size:30px;letter-spacing:.5px}
.brand-dot{width:16px;height:16px;border-radius:50%;background:var(--orange)}
.util-nav{position:absolute;right:88px;top:18px;display:flex;gap:18px;font-size:12px;color:#444;align-items:center}
.util-nav .phone{display:flex;align-items:center;gap:6px;font-weight:600;color:var(--ink)}
.phone-ico{width:20px;height:20px;border-radius:50%;background:var(--orange);display:flex;align-items:center;justify-content:center}
.main-nav{position:absolute;top:56px;left:620px;display:flex;font-size:14px;font-weight:500}
.main-nav a{position:absolute;white-space:nowrap}

/* hero */
.hero{position:absolute;top:88px;left:0;width:1200px;height:590px;overflow:hidden;background:linear-gradient(90deg,#4a1d86 0%,#5a24a0 55%,#6b2bb8 100%)}
.hero-art{position:absolute;left:520px;top:0;width:680px;height:560px;background:radial-gradient(circle at 70% 20%,#b56ad8 0%,#7a3cc0 35%,rgba(90,36,160,0) 70%)}
.hero-title{position:absolute;left:130px;top:160px;width:300px;text-align:center;font-weight:500;line-height:56px}
.hero-title .w{color:var(--white);font-size:44px}
.hero-title .o{color:var(--orange);font-size:44px;text-transform:uppercase;display:block}
.hero-curve{position:absolute;left:0;top:0}

/* intro */
.intro{position:absolute;top:720px;left:0;width:1200px;text-align:center}
.intro h1{font-size:31px;font-weight:500;line-height:44px}
.intro p{font-size:12.5px;line-height:20px;color:#333;width:760px;margin:20px auto 0}
.cta-box{position:absolute;left:307px;top:283px;width:586px;height:70px;border:1px solid #e3e3e3;box-shadow:0 2px 8px rgba(0,0,0,.06);display:flex;align-items:center;justify-content:center;gap:22px;font-size:26px;font-weight:300;color:#222}
.btn{display:inline-block;background:var(--purple);color:var(--white);font-size:12px;border-radius:20px;padding:9px 24px;font-weight:400}

/* service cards */
.service{position:absolute;width:495px;height:375px}
.service-img{position:absolute;left:0;top:0;width:495px;height:307px;border-radius:10px;display:flex;align-items:center;justify-content:center;padding-bottom:90px;color:var(--white);font-size:29px;font-weight:500;letter-spacing:1px}
.service-panel{position:absolute;left:21px;top:211px;width:448px;height:164px;background:var(--white);border-radius:8px;box-shadow:0 4px 14px rgba(0,0,0,.12);display:grid;grid-template-columns:1fr 1fr;padding:30px 30px 20px 32px;row-gap:20px}
.service-item{display:flex;align-items:center;gap:12px;font-size:15px;font-weight:500;line-height:17px}
.svc-ico{width:38px;height:38px;border-radius:50%;background:var(--purple);flex:none;display:flex;align-items:center;justify-content:center}

/* pain band */
.pain-band{position:absolute;top:2013px;left:0;width:1200px;height:399px;background:var(--violet);color:var(--white)}
.pain-col{position:absolute;top:110px;width:420px;text-align:center}
.pain-col h3{font-size:26px;font-weight:500}
.pain-col p{font-size:22px;font-weight:300;font-style:italic;line-height:35px;margin-top:16px;color:#e8def5}
.dots{position:absolute;top:325px;left:566px;display:flex;gap:6px}
.dots span{width:11px;height:11px;border-radius:50%;border:1.5px solid var(--white)}
.dots span.on{border-color:var(--orange)}

/* about */
.about h2{position:absolute;left:88px;top:2496px;font-size:31px;font-weight:500}
.about-text{position:absolute;left:88px;top:2556px;width:460px;font-size:12.5px;line-height:20px;color:#333}
.about-text p+p{margin-top:18px}
.about-img{position:absolute;left:615px;top:2494px;width:497px;height:339px;border-radius:10px;background:linear-gradient(135deg,#d9d3c7,#b9b09b 55%,#8e8a72)}

/* case studies */
.cases{position:absolute;top:2912px;left:0;width:1200px;height:592px;background:var(--grey);color:var(--white)}
.section-title{position:absolute;left:0;width:1200px;text-align:center;font-size:31px;font-weight:500}
.card{position:absolute;width:320px}
.card-img{width:320px;height:235px;border-radius:4px}
.card p{font-size:16px;line-height:24px;margin-top:12px;font-weight:400}
.btn-center{position:absolute;left:539px;width:122px;text-align:center;padding:11px 0}

/* blog */
.post .card-img{height:233px}
.post-date{display:flex;align-items:center;gap:10px;font-size:12px;color:var(--purple);margin-top:18px;font-weight:500}
.post-date .cal{width:20px;height:20px;border-radius:50%;background:#ece6f0;display:flex;align-items:center;justify-content:center}
.post h4{font-size:16px;font-weight:400;line-height:24px;margin-top:10px;color:#222}

/* banner */
.turbo{position:absolute;left:94px;top:4136px;width:1012px;height:72px;border:1px solid #e3e3e3;box-shadow:0 2px 8px rgba(0,0,0,.06);display:flex;align-items:center;justify-content:space-between;padding:0 56px 0 58px;font-size:27px;font-weight:300;color:#222}

/* footer */
.site-footer{position:absolute;top:4270px;left:0;width:1200px;height:573px}
.footer-logo{position:absolute;left:155px;top:230px;color:var(--white);font-size:40px;font-weight:500;display:flex;align-items:center;gap:10px}
.footer-phone{position:absolute;left:163px;top:318px;display:flex;align-items:center;gap:10px;color:var(--white);font-size:17px;font-weight:500}
.fcol{position:absolute;font-size:12.5px;line-height:25px;color:#eadff0}
.fcol h5{color:var(--orange);font-size:15px;font-weight:500;margin-bottom:2px}
.footer-bottom{position:absolute;left:88px;top:517px;width:1024px;border-top:1px solid rgba(255,255,255,.25);padding-top:14px;display:flex;justify-content:space-between;font-size:12.5px;color:#eadff0}
.footer-bottom nav{display:flex;gap:40px}
</style>
</head>
<body>

<header class="site-header">
  <a class="brand" href="#"><span class="brand-dot"></span>Vanta Digital</a>
  <nav class="util-nav">
    <a href="#">Blog</a><a href="#">About Us</a><a href="#">Contact Us</a>
    <span class="phone"><span class="phone-ico"><svg width="11" height="11" viewBox="0 0 24 24"><path fill="#fff" d="M6.6 10.8a15 15 0 0 0 6.6 6.6l2.2-2.2c.3-.3.7-.4 1-.2 1.1.4 2.3.6 3.6.6.6 0 1 .4 1 1V20c0 .6-.4 1-1 1A17 17 0 0 1 3 4c0-.6.4-1 1-1h3.5c.6 0 1 .4 1 1 0 1.3.2 2.5.6 3.6.1.3 0 .7-.2 1z"/></svg></span>01234 567 890</span>
  </nav>
  <nav class="main-nav">
    <a href="#" style="left:0">Create</a>
    <a href="#" style="left:98px">Communicate</a>
    <a href="#" style="left:249px">Convert</a>
    <a href="#" style="left:315px">Close</a>
    <a href="#" style="left:405px">Case Studies</a>
  </nav>
</header>

<section class="hero">
  <div class="hero-art" role="img" aria-label="Illustration of an archer in a purple suit aiming arrows at a target"></div>
  <h1 class="hero-title"><span class="w">Growth Works</span><span class="o">In Your</span><span class="o">Targeting</span></h1>
  <svg class="hero-curve" width="1200" height="590" viewBox="0 0 1200 590">
    <path d="M0 545 Q600 640 1200 500 L1200 590 L0 590 Z" fill="#d8d8d8"/>
    <path d="M0 420 Q300 590 640 575 Q470 600 0 560 Z" fill="#e27927"/>
    <path d="M0 470 Q300 620 720 565 Q980 530 1200 410 L1200 590 L0 590 Z" fill="#fff"/>
  </svg>
</section>

<section class="intro">
  <h1>Fed Up With Agencies Who Don't Care?<br>We've Heard That Before</h1>
  <p style="margin-top:26px">We know every client has unique needs. Yet, few digital agencies spend enough time getting to know the client's business.</p>
  <p>We're different. We take a highly personalised approach to every project, working closely with our clients to understand their objectives, challenges, and target audience.</p>
  <p>Knowing your business is the first step in helping you grow. It's how we work, and it will work for you.</p>
  <div class="cta-box">Achieve Growth That Works <a class="btn" href="#">Set Up a Call</a></div>
</section>

<section class="services">
  <div class="service" style="left:88px;top:1151px">
    <div class="service-img" role="img" aria-label="Photo of hands stacking wooden blocks" style="background:linear-gradient(135deg,#6e5e4c,#3f3a36)">CREATE</div>
    <div class="service-panel">
      <div class="service-item"><span class="svc-ico"><svg width="16" height="16"><circle cx="8" cy="8" r="5" fill="none" stroke="#fff" stroke-width="1.5"/></svg></span>Branding</div>
      <div class="service-item"><span class="svc-ico"><svg width="16" height="16"><path d="M3 13 L8 3 L13 13 Z" fill="none" stroke="#fff" stroke-width="1.5"/></svg></span>Graphics</div>
      <div class="service-item"><span class="svc-ico"><svg width="16" height="16"><rect x="2" y="4" width="9" height="8" fill="none" stroke="#fff" stroke-width="1.5"/><path d="M11 7 L15 5 V11 L11 9" fill="none" stroke="#fff" stroke-width="1.5"/></svg></span>Video</div>
      <div class="service-item"><span class="svc-ico"><svg width="16" height="16"><rect x="3" y="2" width="10" height="12" fill="none" stroke="#fff" stroke-width="1.5"/><path d="M5 6h6M5 9h6" stroke="#fff"/></svg></span>Content</div>
    </div>
  </div>
  <div class="service" style="left:617px;top:1151px">
    <div class="service-img" role="img" aria-label="Photo of colleagues shaking hands in an office" style="background:linear-gradient(135deg,#5a5048,#2f2c2c)">COMMUNICATE</div>
    <div class="service-panel">
      <div class="service-item"><span class="svc-ico"><svg width="16" height="16"><rect x="2" y="3" width="12" height="10" rx="1" fill="none" stroke="#fff" stroke-width="1.5"/></svg></span>Ads</div>
      <div class="service-item"><span class="svc-ico"><svg width="16" height="16"><path d="M3 13 Q3 3 13 3 Q13 13 3 13" fill="none" stroke="#fff" stroke-width="1.5"/></svg></span>Organic</div>
      <div class="service-item"><span class="svc-ico"><svg width="16" height="16"><circle cx="5" cy="6" r="2.5" fill="none" stroke="#fff" stroke-width="1.3"/><circle cx="11" cy="10" r="2.5" fill="none" stroke="#fff" stroke-width="1.3"/></svg></span>Social</div>
      <div class="service-item"><span class="svc-ico"><svg width="16" height="16"><rect x="2" y="4" width="12" height="8" fill="none" stroke="#fff" stroke-width="1.5"/><path d="M2 4 L8 9 L14 4" fill="none" stroke="#fff" stroke-width="1.3"/></svg></span>Email</div>
    </div>
  </div>
  <div class="service" style="left:88px;top:1557px">
    <div class="service-img" role="img" aria-label="Photo of a laptop showing an analytics dashboard" style="background:linear-gradient(135deg,#5c5c58,#2e2e30)">CONVERT</div>
    <div class="service-panel">
      <div class="service-item"><span class="svc-ico"><svg width="16" height="16"><rect x="2" y="3" width="12" height="10" fill="none" stroke="#fff" stroke-width="1.5"/><path d="M2 6h12" stroke="#fff"/></svg></span>Websites</div>
      <div class="service-item"><span class="svc-ico"><svg width="16" height="16"><path d="M2 3 H14 L10 8 V13 L6 11 V8 Z" fill="none" stroke="#fff" stroke-width="1.3"/></svg></span>Lead Generation</div>
      <div class="service-item"><span class="svc-ico"><svg width="16" height="16"><path d="M2 3h2l2 7h7l1-5H5" fill="none" stroke="#fff" stroke-width="1.3"/><circle cx="7" cy="13" r="1" fill="#fff"/><circle cx="12" cy="13" r="1" fill="#fff"/></svg></span>E-commerce</div>
      <div class="service-item"><span class="svc-ico"><svg width="16" height="16"><path d="M3 13V9M7 13V5M11 13V7" stroke="#fff" stroke-width="2"/></svg></span>Analytics</div>
    </div>
  </div>
  <div class="service" style="left:617px;top:1557px">
    <div class="service-img" role="img" aria-label="Photo of hands using a laptop with digital interface overlays" style="background:linear-gradient(135deg,#2c3a4a,#111a26)">CLOSE</div>
    <div class="service-panel">
      <div class="service-item"><span class="svc-ico"><svg width="16" height="16"><circle cx="8" cy="8" r="5.5" fill="none" stroke="#fff" stroke-width="1.3"/><circle cx="8" cy="8" r="2" fill="#fff"/></svg></span>CRM</div>
      <div class="service-item"><span class="svc-ico"><svg width="16" height="16"><circle cx="8" cy="8" r="5" fill="none" stroke="#fff" stroke-width="1.5" stroke-dasharray="3 2"/></svg></span>Systems</div>
      <div class="service-item"><span class="svc-ico"><svg width="16" height="16"><path d="M8 14 L2 8 Q2 3 8 6 Q14 3 14 8 Z" fill="none" stroke="#fff" stroke-width="1.3"/></svg></span>Customer<br>Success</div>
      <div class="service-item"><span class="svc-ico"><svg width="16" height="16"><rect x="4" y="4" width="8" height="8" fill="none" stroke="#fff" stroke-width="1.4"/><path d="M6 2v2M10 2v2M6 12v2M10 12v2M2 6h2M2 10h2M12 6h2M12 10h2" stroke="#fff"/></svg></span>AI &amp;<br>Automations</div>
    </div>
  </div>
</section>

<section class="pain-band">
  <div class="pain-col" style="left:126px"><h3>Your Pain?</h3><p>"I spend most of my development budget fixing errors and bugs"</p></div>
  <div class="pain-col" style="left:653px"><h3>Future Gain</h3><p>A fast and reliable cash- generative content-managed e-commerce or lead generation website</p></div>
  <div class="dots"><span></span><span></span><span class="on"></span><span></span></div>
</section>

<section class="about">
  <h2>Vanta: Where Growth Works</h2>
  <div class="about-text">
    <p>We understand the importance of a strong online presence. That's why we offer a complete range of digital marketing solutions to help you reach your growth goals.</p>
    <p>Our track record demonstrates expertise in all forms of digital mating including Website builds, PPC Ads, SEO, Email Marketing.</p>
    <p>We're constantly staying up-to-date on the latest trends, tech and best practices in the industry, so you can trust that you're getting the most effective and efficient strategies for your business growth.</p>
    <p>Set up a call and we're confident we can show you where we can add growth and value to your business.</p>
  </div>
  <div class="about-img" role="img" aria-label="Photo of a mother and daughter planting seedlings together"></div>
</section>

<section class="cases">
  <h2 class="section-title" style="top:72px">Case Studies</h2>
  <div class="card" style="left:88px;top:145px"><div class="card-img" role="img" aria-label="Photo of business people shaking hands" style="background:linear-gradient(135deg,#b8a48c,#6e5e50)"></div><p>Lorem Ipsum is simply dummy text of the printing industry.</p></div>
  <div class="card" style="left:440px;top:145px"><div class="card-img" role="img" aria-label="Photo of a laptop with a data dashboard" style="background:linear-gradient(135deg,#dcdcd6,#8c9490)"></div><p>Lorem Ipsum is simply dummy text of the printing industry.</p></div>
  <div class="card" style="left:792px;top:145px"><div class="card-img" role="img" aria-label="Photo of a hand building a wooden block tower" style="background:linear-gradient(135deg,#e6e0d6,#a88c68)"></div><p>Lorem Ipsum is simply dummy text of the printing industry.</p></div>
  <a class="btn btn-center" href="#" style="top:494px">View All</a>
</section>

<section class="blog">
  <h2 class="section-title" style="top:3575px">From the Blog</h2>
  <div class="card post" style="left:88px;top:3651px"><div class="card-img" role="img" aria-label="Photo of a businessman presenting a search engine logo" style="background:linear-gradient(135deg,#2a2a2a,#0c0c0c)"></div><div class="post-date"><span class="cal"><svg width="10" height="10"><rect x="1" y="2" width="8" height="7" fill="none" stroke="#5c306b"/></svg></span>2 June, 2023</div><h4>Seekly's New PPC Features are Loaded with AI</h4></div>
  <div class="card post" style="left:440px;top:3651px"><div class="card-img" role="img" aria-label="Photo of a magnifying glass over search-related keywords" style="background:linear-gradient(135deg,#e0e0e0,#6a6a6a)"></div><div class="post-date"><span class="cal"><svg width="10" height="10"><rect x="1" y="2" width="8" height="7" fill="none" stroke="#5c306b"/></svg></span>2 June, 2023</div><h4>How Seekly Killed the Broad Match Keyword?</h4></div>
  <div class="card post" style="left:792px;top:3651px"><div class="card-img" role="img" aria-label="Photo of a smartphone surrounded by social media notifications" style="background:linear-gradient(135deg,#8aa05c,#c8703a)"></div><div class="post-date"><span class="cal"><svg width="10" height="10"><rect x="1" y="2" width="8" height="7" fill="none" stroke="#5c306b"/></svg></span>2 June, 2023</div><h4>The 9 Rules of Social Media Engagement (Part II)</h4></div>
  <a class="btn btn-center" href="#" style="top:4017px">View All</a>
</section>

<div class="turbo">We're the turbo boost for your digital marketing engine <a class="btn" href="#">Put Your Foot Down</a></div>

<footer class="site-footer">
  <svg class="abs" style="left:0;top:0" width="1200" height="573" viewBox="0 0 1200 573">
    <path d="M0 150 Q500 -20 1200 40 L1200 573 L0 573 Z" fill="#cacaca"/>
    <path d="M0 140 Q560 -10 1200 10 L1200 573 L0 573 Z" fill="#e27927"/>
    <path d="M0 160 Q600 20 1200 70 L1200 573 L0 573 Z" fill="#5c306b"/>
  </svg>
  <div class="footer-logo"><span class="brand-dot" style="width:18px;height:18px"></span>Vanta Digital</div>
  <div class="footer-phone"><span class="phone-ico" style="width:28px;height:28px"><svg width="14" height="14" viewBox="0 0 24 24"><path fill="#fff" d="M6.6 10.8a15 15 0 0 0 6.6 6.6l2.2-2.2c.3-.3.7-.4 1-.2 1.1.4 2.3.6 3.6.6.6 0 1 .4 1 1V20c0 .6-.4 1-1 1A17 17 0 0 1 3 4c0-.6.4-1 1-1h3.5c.6 0 1 .4 1 1 0 1.3.2 2.5.6 3.6.1.3 0 .7-.2 1z"/></svg></span>01234 567 890</div>
  <div class="fcol" style="left:455px;top:162px"><h5>Create</h5>Branding<br>Graphics<br>Video<br>Content</div>
  <div class="fcol" style="left:686px;top:162px"><h5>Convert</h5>Websites<br>Lead Generation<br>Ecommerce<br>Analytics</div>
  <div class="fcol" style="left:920px;top:162px"><h5>Connect</h5>Case Studies<br>Blog<br>About Us</div>
  <div class="fcol" style="left:455px;top:318px"><h5>Communicate</h5>Ads<br>Organic<br>Social<br>Email</div>
  <div class="fcol" style="left:686px;top:318px"><h5>Close</h5>CRM<br>Systems<br>Customer Success<br>AI &amp; Automations</div>
  <div class="fcol" style="left:920px;top:318px"><h5>Address</h5>Kestrel House<br>Midford<br>Wessex<br>MF1 2AB</div>
  <div class="footer-bottom"><span>© 2023 Vanta Digital Limited. All rights reserved</span><nav><a href="#">Sitemap</a><a href="#">Terms of Use</a><a href="#">Privacy Policy</a></nav></div>
</footer>

</body>
</html>
```